KELVARA Branded Wellness Pouch Design for Clinical Study Kit

Overview:
We are creating custom zippered pouches for our “KELVARA Study Fuel Kits,” which will be distributed to physicians, nurses, and research coordinators participating in a national clinical study. We need a clean, professional design for the front of the pouch that incorporates our existing KELVARA logo and the new supporting text.
Design Requirements:
Keep the existing KELVARA logo intact (we’ll upload the file).
Add the text “Study Fuel Kit” immediately following the logo, using the same or a complementary font.
Add a tagline below that reads:
Power up. Kelvara. Go again.
Use a layout that looks balanced, legible, and polished when printed on a small pouch.
Stay consistent with our brand color palette (blue from the logo)
The overall style should feel modern, wellness-driven, and professional — think premium, science-forward, and sleek.
Audience:
This kit will be given to medical professionals, so the design should feel elevated and credible (not flashy or overly playful).
Deliverables:
Vector file (AI, EPS)
It is a frosted white, zippered vinyl pouch (9 1/2 " x 8 1/4 " x 2 1/2 ")
The imprint size is (6 3/4" W x 4 1/2" H)
The imprint can only be 1-color, so in this case - we would like the color to be the dark blue (#06173c)

```html
<!DOCTYPE html>
<html lang="en">
<head>
<meta charset="utf-8">
<title>KELVARA Study Fuel Kit – Pouch Imprint</title>
<link rel="stylesheet" href="https://fonts.googleapis.com/css2?family=Archivo+Black&family=Oswald:wght@400;600&display=swap">
<style>
  :root {
    --ink: #272a6a;
    --paper: #ffffff;
    --card-edge: #ececec;
  }
  html, body {
    margin: 0;
    width: 1200px;
    height: 1000px;
    overflow: hidden;
    background: var(--paper);
  }
  .imprint {
    display: block;
    width: 1200px;
    height: 1000px;
  }
  .imprint-frame { fill: var(--paper); stroke: var(--card-edge); stroke-width: 1.5; }
  .brand-mark { fill: var(--ink); }
  .brand-name { font-family: "Oswald", sans-serif; font-weight: 400; fill: var(--ink); }
  .brand-descriptor { font-family: "Oswald", sans-serif; font-weight: 400; fill: var(--ink); }
  .kit-title { font-family: "Oswald", sans-serif; font-weight: 600; fill: var(--ink); }
  .title-divider { fill: var(--ink); }
  .tagline-word { font-family: "Archivo Black", sans-serif; fill: var(--ink); }
  .tagline-rule { fill: var(--ink); }
</style>
</head>
<body>
<svg class="imprint" viewBox="0 0 1200 1000" xmlns="http://www.w3.org/2000/svg" role="img" aria-label="KELVARA U.S. Study Fuel Kit — Power up. Kelvara. Go again.">
  <defs>
    <clipPath id="imprint-area">
      <rect x="109" y="182" width="980" height="653"/>
    </clipPath>
  </defs>

  <rect class="imprint-frame" x="109" y="182" width="980" height="653"/>

  <g clip-path="url(#imprint-area)">
    <!-- Brand lockup -->
    <rect class="brand-mark" x="134" y="312" width="62" height="62"/>
    <text class="brand-name" x="222" y="388" font-size="128" textLength="550" lengthAdjust="spacingAndGlyphs">KELVARA U.S.</text>
    <text class="brand-descriptor" x="224" y="416" font-size="17" textLength="547" lengthAdjust="spacingAndGlyphs">Nuvia Core NP Randomized, Sham-Controlled, Multi-Center, Double Blind Clinical Trial</text>

    <rect class="title-divider" x="804" y="289" width="4" height="127"/>

    <text class="kit-title" x="840" y="342" font-size="66" textLength="176" lengthAdjust="spacingAndGlyphs">STUDY</text>
    <text class="kit-title" x="840" y="414" font-size="66" textLength="237" lengthAdjust="spacingAndGlyphs">FUEL KIT</text>

    <!-- Tagline stack -->
    <text class="tagline-word" x="222" y="580" font-size="112">POWER UP.</text>
    <rect class="tagline-rule" x="118" y="605" width="971" height="4"/>
    <text class="tagline-word" x="222" y="706" font-size="112">KELVARA.</text>
    <rect class="tagline-rule" x="118" y="730" width="971" height="4"/>
    <text class="tagline-word" x="222" y="832" font-size="112">GO AGAIN.</text>
  </g>
</svg>
</body>
</html>
```